April 11th Event- Islamorada- Coaching/Tarot/Hypnotherapy

Hi! Need a flyer that can also be posted on social media. Directions attached. Also will need a version that 2 can fit on 1 piece of paper so I can cut in half for hand outs. PDF example attached as well so you can understand. Thank you!

AAAAAAAAAAAAAAAAAAAAAAAAAAAAAAAAAAAAAAAAAAAAAAAAAAAAAAAAAAAAAAAAAAAAAAAAAAAAAAAAAAAAAAAAAAAAAAAAAAAAAAAAAAAAAAAAAAAAAAAAAAAAAAAAAAAAAAAAAAAAAAAAAAAAAAAAAAAAAAAAAAAAAAAAAAAAAAAAAAAAAAAAAAAAAAAAAAAAAAAAAAAAAAAAAAAAAAAAAAAAAAAAAA

Target Market(s)

Female audience age 35-70.
Spiritual, sophisticated

Industry/Entity Type

Event Planning

Font styles to use
Serif

Colors
d2a4cc
3176b5
85acd3
b868aa
e667a6
eea4c8
f59296
fbf289
add136

Requirements
Must have
• See attachments
Nice to have
• See attachments

```html
<!DOCTYPE html>
<html lang="en">
<head>
<meta charset="utf-8">
<title>Get The 411 – Evening Flyer</title>
<link rel="stylesheet" href="https://fonts.googleapis.com/css2?family=Oswald:wght@400;500;700&family=Lato:wght@400;700&family=Titillium+Web:ital,wght@1,600&display=swap">
<style>
:root{
  --magenta-deep:#8e2f8a;
  --magenta:#b23f96;
  --pink:#e85aa3;
  --blue:#2f76b5;
  --link-blue:#2a73c0;
  --plum:#8b2f83;
  --paper:#ffffff;
  --wave-tint:#eaf2fa;
  --ink:#111111;
}
*{margin:0;padding:0;box-sizing:border-box}
html,body{width:902px;height:1200px;overflow:hidden;background:var(--paper)}
.flyer{position:relative;width:902px;height:1200px;overflow:hidden;background:var(--paper);color:var(--ink);font-family:'Lato',sans-serif}
.wave-field{position:absolute;inset:0;background:linear-gradient(180deg,var(--wave-tint),#f7fafd 60%,var(--wave-tint))}
.hero-band{position:absolute;left:0;top:0;width:902px;height:813px}
.abs{position:absolute}
.date-badge{left:52px;top:49px;width:167px;height:126px;background:var(--blue);border:2px solid #fff;color:#fff}
.date-day{left:10px;top:2px;font:700 78px/1 'Oswald',sans-serif;transform:scaleX(.85);transform-origin:left}
.date-suffix{left:75px;top:14px;font:500 28px/1 'Oswald',sans-serif}
.date-month{left:75px;top:46px;font:500 34px/1 'Oswald',sans-serif}
.date-weekday{left:0;width:163px;top:87px;text-align:center;font:400 27px/1 'Lato',sans-serif;letter-spacing:.5px}
.headline{left:44px;top:192px;color:#fff;font:700 120px/1.1 'Oswald',sans-serif;letter-spacing:-3px;white-space:nowrap;transform:scaleX(.85);transform-origin:left}
.subhead{left:44px;top:306px;color:#fff;font:700 48px/1.1 'Oswald',sans-serif;letter-spacing:-.5px;white-space:nowrap;transform:scaleX(.87);transform-origin:left}
.rule{left:44px;width:486px;height:3px;background:#fff}
.invite{left:44px;top:400px;color:#fff;font:italic 600 38px/48px 'Titillium Web',sans-serif}
.speakers-title{left:44px;top:535px;color:#fff;font:400 29px/1.2 'Oswald',sans-serif}
.speaker-list{left:72px;top:580px;list-style:none;color:#fff}
.speaker-list li{height:48px;white-space:nowrap;font:400 19px/48px 'Lato',sans-serif}
.speaker-list li::before{content:"•";margin-right:12px;font-size:18px}
.speaker-name{font:500 29px/1 'Oswald',sans-serif;letter-spacing:-.8px}
.info-badge{width:126px;height:126px;border-radius:50%;background:var(--blue);color:#fff;text-align:center}
.info-badge svg{position:absolute;left:42px;top:18px}
.info-badge span{position:absolute;left:0;right:0;top:76px;font:500 19px/1 'Oswald',sans-serif}
.time-text{left:40px;width:410px;top:882px;text-align:center}
.time-main{font:700 33px/1.2 'Lato',sans-serif}
.time-sub{font:400 25px/1.2 'Lato',sans-serif}
.divider{left:452px;top:876px;width:3px;height:81px;background:var(--ink)}
.venue-text{left:480px;width:390px;top:886px;text-align:center;font:400 21px/26px 'Lato',sans-serif}
.venue-note{font-size:17px;line-height:22px}
.ticket-frame{left:39px;top:1000px;width:832px;height:128px;border:3px solid var(--magenta);border-radius:26px;background:#fff}
.ticket-pill{left:158px;top:976px;width:588px;height:62px;border-radius:31px;background:linear-gradient(90deg,var(--magenta-deep),var(--pink));color:#fff;text-align:center;white-space:nowrap}
.ticket-price{font:700 46px/62px 'Lato',sans-serif}
.ticket-note{font:700 16px/1 'Lato',sans-serif}
.guest-note{left:39px;width:832px;top:1053px;text-align:center;font:400 23px/1.2 'Lato',sans-serif}
.contact-line{left:39px;width:832px;top:1083px;text-align:center;white-space:nowrap;font:400 21px/1.3 'Oswald',sans-serif;letter-spacing:-.4px}
.contact-email{color:var(--link-blue);font-size:27px;font-weight:500}
.contact-phone{color:var(--plum);font-size:27px;font-weight:500}
.signoff{right:45px;top:1141px;font:400 15px/1 'Lato',sans-serif}
</style>
</head>
<body>
<main class="flyer">
  <div class="wave-field" role="img" aria-label="Soft pale blue wave pattern background"></div>

  <svg class="hero-band" viewBox="0 0 902 813" aria-hidden="true">
    <defs>
      <linearGradient id="heroGrad" x1="0" y1="0" x2="1" y2="0.35">
        <stop offset="0" stop-color="#8e2f8a"/>
        <stop offset="0.55" stop-color="#c2449b"/>
        <stop offset="1" stop-color="#ec5ca4"/>
      </linearGradient>
      <linearGradient id="heroShade" x1="0" y1="0" x2="0" y2="1">
        <stop offset="0.45" stop-color="#8e2f8a" stop-opacity="0"/>
        <stop offset="1" stop-color="#8e2f8a" stop-opacity="0.75"/>
      </linearGradient>
    </defs>
    <polygon points="0,0 368,0 902,321 902,813 0,813" fill="url(#heroGrad)"/>
    <polygon points="0,0 368,0 902,321 902,813 0,813" fill="url(#heroShade)"/>
  </svg>

  <div class="abs date-badge">
    <div class="abs date-day">11</div>
    <div class="abs date-suffix">th</div>
    <div class="abs date-month">APRIL</div>
    <div class="abs date-weekday">THURSDAY</div>
  </div>

  <h1 class="abs headline">GET THE 411-</h1>
  <h2 class="abs subhead">Open Yourself Up To The Info You Have Inside</h2>

  <div class="abs rule" style="top:394px"></div>
  <p class="abs invite">Please Join Us For An Evening of<br>Self Discovery, and Enlightment and Fun!</p>
  <div class="abs rule" style="top:502px"></div>

  <h3 class="abs speakers-title">Speakers:</h3>
  <ul class="abs speaker-list">
    <li><span class="speaker-name">Lena Marsh</span>- The Bright Path Life Coach- Certified Professional Life Coach</li>
    <li><span class="speaker-name">Dana Whitfield</span>- Licensed Hypnotherapist- Willow Holistic Gifts and Therapies</li>
    <li><span class="speaker-name">Rosa Kellam</span>- Tarot Readings/ True North Spiritual Counselor</li>
  </ul>

  <div class="abs info-badge" style="left:183px;top:747px">
    <svg width="42" height="42" viewBox="0 0 42 42" aria-hidden="true">
      <circle cx="21" cy="21" r="19" fill="#fff"/>
      <path d="M21 9v13l7 6" fill="none" stroke="#2f76b5" stroke-width="4" stroke-linecap="round"/>
    </svg>
    <span>Time:</span>
  </div>
  <div class="abs info-badge" style="left:592px;top:747px">
    <svg width="42" height="46" viewBox="0 0 42 46" aria-hidden="true">
      <path d="M21 2C11 2 4 9.5 4 19c0 12 17 25 17 25s17-13 17-25C38 9.5 31 2 21 2z" fill="#fff"/>
      <circle cx="21" cy="19" r="7" fill="#2f76b5"/>
    </svg>
    <span>Where:</span>
  </div>

  <div class="abs time-text">
    <div class="time-main">Doors Open at 5:30.</div>
    <div class="time-sub">Event from 6pm-8pm.</div>
  </div>
  <div class="abs divider"></div>
  <div class="abs venue-text">
    The Gardens at Seabright- 40210<br>Coral Way Islamorada<br>
    <span class="venue-note">(MM40 Bayside behind Harbor Market)</span>
  </div>

  <div class="abs ticket-frame"></div>
  <div class="abs ticket-pill"><span class="ticket-price">Tickets $15 each.</span><span class="ticket-note">( Drinks included.)</span></div>
  <p class="abs guest-note">Names must be on the guest list</p>
  <p class="abs contact-line">Contact Lena Marsh for tickets : <span class="contact-email">lena@brightpathcoach.com/</span> <span class="contact-phone">305-555-0148</span></p>

  <p class="abs signoff">Hope to see you there!</p>
</main>
</body>
</html>
```